MARBLEQUILL Non-Profit- Pitch Deck needs visual boost

PLEASE CHECK FILE 6 for most current version of Pitch Deck that needs editing. Made some final edits compared to first one uploaded yesterday.

We need to have someone come in and inject our pitch deck with some design and graphic love. The content and words are there but we need it to look sharper, cleaner, and more visually striking. The Non-profit is managing the cleanup of 360 million tonnes of CO2 before the year 2025. We need it to be editable and customizable moving forward so no PDF versions, PP and Keynote only. Please ignore scatch notes after pg 15 .

attachted ex summary in additional uploads for more information.
Check out website too 7386.com

Target Market(s)

Potential partners and investors

Industry/Entity Type

Sustainability

Font styles to use
Sans Serif

Colors

Designer to choose colors to be used in the design.

Requirements
Must have
• Simplified version of current slideshow- Less noise in the deck espcially on logo page.
• Copyright version must be easily editable. Not adobe. PP or Keynote

```html
<!DOCTYPE html>
<html lang="en">
<head>
<meta charset="utf-8">
<title>MarbleQuill – Pitch Deck Pages</title>
<link rel="stylesheet" href="https://fonts.googleapis.com/css2?family=Montserrat:wght@400;600;700&family=Questrial&display=swap">
<style>
:root{
  --bg:#e4e4e4;
  --paper:#ffffff;
  --ink:#1d1d1d;
  --muted:#5a5a5a;
  --soft:#ececec;
  --teal:#1f9a8a;
  --green:#3bbf7a;
  --orange:#f5a623;
  --blue:#3b7fe0;
  --mint:#7fe0b0;
  --sky:#2ea6e0;
  --tab:#2a2a2a;
}
*{box-sizing:border-box;margin:0;padding:0}
html,body{width:1200px;height:2394px;overflow:hidden}
body{background:var(--bg);font-family:"Questrial",Arial,sans-serif;color:var(--ink);position:relative}
.sheet{position:absolute;background:var(--paper);box-shadow:0 6px 18px rgba(0,0,0,.18);overflow:hidden}
.tab{position:absolute;background:var(--tab)}
.tab.grey{background:#777}
h1,h2,h3{font-family:"Montserrat",Arial,sans-serif}

/* Cover */
.cover{left:330px;top:100px;width:540px;height:800px}
.cover .intro{position:absolute;left:40px;top:92px;width:420px;font-size:18px;line-height:1.3}
.cover .photo{position:absolute;left:30px;right:30px;top:190px;height:340px;
  background:linear-gradient(180deg,#e7c02a 0%,#c9a83a 28%,#8d8a4a 52%,#3e4a2e 70%,#6f8a2a 85%,#a3b23a 100%)}
.cover .statement{position:absolute;left:40px;width:320px;font-size:16px;line-height:1.3;color:var(--muted)}
.cover .statement b{display:block;font-family:"Montserrat",Arial,sans-serif;color:var(--ink);font-size:18px}
.cover .statement b::before{content:"›";margin-right:8px;font-size:22px}
.cover .brand{position:absolute;right:36px;top:640px;display:flex;align-items:center;gap:10px;font-size:20px;font-weight:700;font-family:"Montserrat",Arial,sans-serif}
.cover .brand i{width:30px;height:30px;border-radius:50%;background:var(--ink);display:block}
.url{position:absolute;font-family:"Montserrat",Arial,sans-serif;font-weight:700}
.cover .url{left:40px;top:744px;font-size:16px}

/* Deck pages */
.page{width:348px;height:626px}
.page h2{position:absolute;left:22px;top:22px;width:260px;font-size:11px;line-height:1.3;font-weight:700}
.page .subtitle{position:absolute;left:22px;font-size:9.5px;font-weight:700;color:var(--teal);font-family:"Montserrat",Arial,sans-serif}
.stage{position:absolute;right:14px;top:18px;width:40px;text-align:center;font-size:6px;color:var(--green)}
.stage i{display:block;width:16px;height:16px;border-radius:50%;border:2px solid currentColor;margin:0 auto 3px}
.haze{position:absolute;left:0;right:0;height:160px;background:linear-gradient(180deg,rgba(230,230,230,0),#e6e6e6 60%,#dcdcdc)}
.footer{position:absolute;left:0;right:0;bottom:0;height:50px;background:var(--paper)}
.footer .url{left:20px;top:20px;font-size:8px}
.footer .name{position:absolute;right:20px;top:17px;font-size:11px;font-weight:700;font-family:"Montserrat",Arial,sans-serif}

.pillars{position:absolute;left:14px;right:14px;top:92px;display:flex;gap:6px}
.pillar{flex:1;border-radius:8px;padding:6px;height:124px;position:relative}
.pillar .num{position:absolute;left:-3px;top:-8px;width:14px;height:14px;border-radius:3px;background:#fff;border:1.5px solid currentColor;font-size:8px;text-align:center;line-height:11px;font-weight:700;color:var(--ink)}
.pillar .card{background:#fff;height:100%;padding:8px 6px;font-size:6.5px;line-height:1.35;text-align:center;color:var(--muted)}
.pillar .card b{display:block;font-size:7px;color:var(--ink);margin:4px 0 6px;font-family:"Montserrat",Arial,sans-serif}
.p-orange{background:var(--orange)} .p-blue{background:var(--blue)} .p-mint{background:var(--mint)}

.reach{position:absolute;left:24px;right:24px;top:232px;height:172px;background:#fff;border-radius:10px;box-shadow:0 2px 8px rgba(0,0,0,.12);text-align:center;padding-top:10px}
.reach h3{font-size:8px}
.reach p{font-size:7px;color:var(--muted)}
.marks{display:flex;flex-wrap:wrap;justify-content:center;gap:8px 10px;margin-top:10px;padding:0 14px}
.marks span{width:46px;height:16px;border-radius:3px;background:#cfd4d8}
.marks span:nth-child(3n){background:#d9c8c8}
.marks span:nth-child(4n){width:20px;border-radius:50%}
.partners{position:absolute;left:18px;top:424px;font-size:6.5px;font-weight:700}
.badges{position:absolute;left:18px;top:442px;display:flex;gap:8px}
.badges span{width:20px;height:20px;border-radius:50%;background:#9aa0a6}
.quote{position:absolute;right:18px;top:418px;width:170px;font-size:6.5px;line-height:1.4;text-align:right;color:var(--muted)}
.quote b{color:var(--ink)}

.claim{position:absolute;left:22px;top:62px;font-size:8.5px;font-style:italic;color:var(--teal);font-weight:700;width:260px;font-family:"Montserrat",Arial,sans-serif}
.center{position:absolute;left:0;right:0;text-align:center;font-size:7.5px;color:var(--muted)}
.equation{position:absolute;left:22px;top:146px;display:flex;align-items:center;gap:5px;font-size:9px}
.equation .ring{width:38px;height:38px;border-radius:50%;border:1.5px solid var(--teal);display:flex;align-items:center;justify-content:center}
.equation b{font-size:8.5px;line-height:1.3;font-family:"Montserrat",Arial,sans-serif;margin-left:4px}
.icons{position:absolute;left:0;right:0;top:232px;display:flex;justify-content:center;gap:14px}
.insights{position:absolute;left:24px;right:24px;top:318px;height:120px;background:#fff;border-radius:10px;box-shadow:0 2px 8px rgba(0,0,0,.12)}
.chart{position:absolute;left:12px;top:18px;width:150px;height:88px;background:#245a62}
.phone{position:absolute;right:16px;top:10px;width:108px;height:100px;border-radius:12px;border:3px solid #cfd4d8;background:linear-gradient(160deg,#b48aa0,#7a6f8c 55%,#4d5f7a)}
.toast{position:absolute;right:22px;top:76px;width:96px;background:#1f5f6a;color:#fff;font-size:5.5px;padding:3px 4px;border-radius:3px;line-height:1.3}

.table{position:absolute;left:14px;right:14px;top:82px;border-radius:8px;overflow:hidden;display:grid;grid-template-columns:1fr 1fr 1fr 1fr}
.table .th{background:var(--sky);color:#fff;font-size:6.5px;font-weight:700;text-align:center;padding:6px 2px;height:30px;display:flex;align-items:center;justify-content:center;font-family:"Montserrat",Arial,sans-serif}
.col{font-size:6px;line-height:1.4;padding:5px;color:var(--muted);height:318px;position:relative}
.col.dark{background:#d9d9d9}
.col p{margin-bottom:8px}
.col .note{background:#fff;padding:4px;border-radius:3px;color:var(--ink)}
.shot{height:100px;margin-bottom:4px}
.col.partners-col{text-align:center}
.col.partners-col b{display:block;color:var(--ink);font-size:6.5px;margin:6px 0 2px}
.band{grid-column:1/5;background:var(--sky);color:#fff;font-size:6px;text-align:center;padding:5px 30px}
</style>
</head>
<body>

<!-- Cover sheet -->
<section class="sheet cover">
  <div class="tab grey" style="right:0;top:40px;width:16px;height:44px"></div>
  <p class="intro">In response to the realities of our changing world, MarbleQuill is 7 year challenge driving responsibility for our CO2 footprint.</p>
  <div class="photo" role="img" aria-label="Golden sunrise over misty mountain ridges, dark forest and a green meadow"></div>
  <div class="statement" style="top:556px"><b>OUR MISSION:</b>To provide individuals and businesses with energy and CO2 reduction solutions.</div>
  <div class="statement" style="top:636px"><b>OUR GOAL:</b>Mobilize the 'clean-up' of 360 million tons of CO2 by 2025.</div>
  <div class="brand"><i></i>MarbleQuill</div>
  <div class="tab" style="left:0;top:736px;width:18px;height:32px"></div>
  <span class="url">www.marblequill.com</span>
</section>

<!-- Page: engagement -->
<section class="sheet page" style="left:137px;top:1050px">
  <div class="tab" style="left:0;top:22px;width:8px;height:26px"></div>
  <h2>We target systemic behavior change by applying gamification to the CSR / Employee Engagement Gap</h2>
  <div class="stage"><i></i>Integrate</div>
  <p class="subtitle" style="top:66px">MarbleQuill Enterprise 360 Net Zero Challenge:</p>
  <div class="pillars">
    <div class="pillar p-orange"><span class="num">1</span><div class="card"><b>SCALABLE</b>App model is user-friendly; provides superior sustainability data to CSR departments; modular for easy customizability</div></div>
    <div class="pillar p-blue"><span class="num">2</span><div class="card"><b>GAMIFIED</b>App model is user-friendly; provides superior sustainability data to CSR departments; modular for easy customizability</div></div>
    <div class="pillar p-mint"><span class="num">3</span><div class="card"><b>EFFECTIVE</b>Proven model for reducing emissions; lower operational costs, greener supply chain, improved employee morale, health outcomes, and brand reputation</div></div>
  </div>
  <div class="haze" style="top:300px"></div>
  <div class="reach">
    <h3>IN 2017 WE REACHED 75K+ EMPLOYEES:</h3>
    <p>20 Fortune 500 organizations-</p>
    <div class="marks"><span></span><span></span><span></span><span></span><span></span><span></span><span></span><span></span><span></span><span></span><span></span><span></span><span></span></div>
  </div>
  <p class="partners">...&amp; 100's of Non-profits and Schools</p>
  <div class="badges"><span></span><span></span><span></span><span></span></div>
  <p class="quote">"Northbank sees great value in relationships that help us tap into employee motivation for fun, impactful sustainability engagement - <b>exactly what MarbleQuill offers.</b>"<br><b>Mira Solano,</b><br>Head of CSR at Northbank UK</p>
  <footer class="footer"><div class="tab" style="left:0;top:14px;width:8px;height:22px"></div><span class="url">www.marblequill.com</span><span class="name">MarbleQuill</span></footer>
</section>

<!-- Page: tracker -->
<section class="sheet page" style="left:622px;top:1050px">
  <div class="tab" style="left:0;top:22px;width:8px;height:26px"></div>
  <h2>We are developing a convenient emissions footprint tracker for the mass market with our tech partners</h2>
  <div class="stage"><i></i>Integrate</div>
  <p class="claim">"You're on track to reduce your CO2 impact by 12% this month, and 50% this year!"</p>
  <p class="center" style="top:118px;font-weight:700;color:var(--ink)">App automatically analyzes spending &amp; GPS to extract CO2e insights...</p>
  <div class="equation">
    <span class="ring"><svg width="16" height="20" viewBox="0 0 16 20"><rect x="2" y="1" width="12" height="18" rx="2" fill="none" stroke="#333" stroke-width="1.5"/><circle cx="8" cy="16" r="1" fill="#333"/></svg></span>+
    <span class="ring"><svg width="20" height="16" viewBox="0 0 20 16"><rect x="1" y="2" width="18" height="12" rx="2" fill="none" stroke="#333" stroke-width="1.5"/><line x1="1" y1="6" x2="19" y2="6" stroke="#333" stroke-width="1.5"/></svg></span>+
    <span class="ring"><svg width="18" height="18" viewBox="0 0 18 18"><path d="M9 2a5 5 0 0 1 5 5c0 4-5 9-5 9s-5-5-5-9a5 5 0 0 1 5-5z" fill="none" stroke="#333" stroke-width="1.5"/><circle cx="9" cy="7" r="1.6" fill="#333"/></svg></span>
    <b>= 18 TONS OF CO2E /YEAR<br>(AVERAGE USA)</b>
  </div>
  <p class="center" style="top:200px">...provides nudges, points and financial incentives for reaching Net Zero Target</p>
  <div class="icons">
    <svg width="18" height="16" viewBox="0 0 18 16"><path d="M9 2 1 6l8 4 8-4zM4 8v4c3 2 7 2 10 0V8" fill="#333"/></svg>
    <svg width="16" height="18" viewBox="0 0 16 18"><rect x="2" y="2" width="6" height="15" fill="#333"/><rect x="9" y="7" width="5" height="10" fill="#777"/></svg>
    <svg width="18" height="18" viewBox="0 0 18 18"><path d="M2 11l14-7-3 9-4-3-3 4v-5z" fill="#333"/></svg>
    <svg width="16" height="18" viewBox="0 0 16 18"><path d="M2 1h9l3 3v13H2z" fill="#333"/><path d="M5 12l3-5 3 5" stroke="#fff" fill="none"/></svg>
    <svg width="18" height="18" viewBox="0 0 18 18"><circle cx="11" cy="3" r="2" fill="#333"/><path d="M3 17l5-7 3 3 3-6" stroke="#333" stroke-width="2" fill="none"/></svg>
  </div>
  <p class="center" style="top:258px">Gamified behavioral science for carbon positive action across education, business, travel, policy &amp; lifestyle</p>
  <div class="haze" style="top:270px"></div>
  <div class="insights">
    <svg class="chart" viewBox="0 0 150 88">
      <rect width="150" height="88" fill="#245a62"/>
      <g fill="#b7cf3a"><rect x="14" y="14" width="14" height="58"/><rect x="42" y="38" width="14" height="34"/><rect x="70" y="28" width="14" height="44"/><rect x="98" y="44" width="14" height="28"/><rect x="124" y="36" width="14" height="36"/></g>
      <g fill="#d8e86a"><rect x="14" y="12" width="14" height="3"/><rect x="42" y="36" width="14" height="3"/><rect x="70" y="26" width="14" height="3"/><rect x="98" y="42" width="14" height="3"/><rect x="124" y="34" width="14" height="3"/></g>
      <g fill="#fff" font-size="5" font-family="Questrial,sans-serif"><text x="16" y="82">Food</text><text x="42" y="82">Shelter</text><text x="70" y="82">Mobility</text><text x="98" y="82">Goods</text><text x="122" y="82">Services</text></g>
    </svg>
    <div class="phone" role="img" aria-label="Phone screen showing the tracking app with a blurred colourful wallpaper"></div>
    <div class="toast">Well done! Your logged reductions have earned you a bonus on a CO2 friendly good</div>
  </div>
  <footer class="footer"><div class="tab" style="left:0;top:14px;width:8px;height:22px"></div><span class="url">www.marblequill.com</span><span class="name">MarbleQuill</span></footer>
</section>

<!-- Page: restore -->
<section class="sheet page" style="left:380px;top:1717px">
  <div class="tab" style="left:0;top:22px;width:8px;height:26px"></div>
  <h2>Our platform matches Net Zero targets with scalable CO2 reduction projects</h2>
  <div class="stage" style="color:var(--sky)"><i></i>Restore</div>
  <p class="subtitle" style="top:62px;font-size:7.5px">One-click access to select CO2 'clean-up' projects to balance your carbon footprint</p>
  <div class="table">
    <div class="th">Your Impact Donation</div><div class="th">Focus Areas</div><div class="th">Implementing Partners</div><div class="th">Impact</div>
    <div class="col dark">
      <p>Impact metrics offer choice for achieving CO2 neutrality</p>
      <p>Simple, tax-deductible donation to verified projects</p>
      <p>Exclusive stories &amp; VR content from the front-line of projects driving change</p>
      <p class="note">"Your $100 rainforest conservation donation cleared the remaining 9 tons of CO2 of your Net Zero target &amp; was matched by your employer. You are a carbon negative human."</p>
    </div>
    <div class="col">
      <div class="shot" role="img" aria-label="Aerial view of green rainforest" style="background:linear-gradient(160deg,#5f8f3a,#2f6a2a 60%,#8fae5a)"></div>
      <div class="shot" role="img" aria-label="Blue ocean wave" style="background:linear-gradient(160deg,#0f5f8f,#2ea6d0 55%,#dff3fb)"></div>
      <div class="shot" role="img" aria-label="Blue sky with white clouds" style="background:linear-gradient(180deg,#4a8fd0,#a9cdee 60%,#eef5fb)"></div>
    </div>
    <div class="col partners-col">
      <b>Timberroot</b>
      <p>Focus on afforestation, conservation, and biochar</p>
      <b>Deep Tide</b>
      <b>The Clear Horizon Foundation</b>
      <p>Focus on ocean plastic clean-up and kelp/algae farming</p>
      <b>Airloop</b>
    </div>
    <div class="col" style="text-align:center">
      <p>1 tree (40 years) = ~1 tCO2 captured</p>
      <p style="margin-top:24px">1 acre of seaweed = Up to 68 tCO2 / yr</p>
      <p style="margin-top:24px">$94 - $232 / tCO2 Filtrating CO2 out of the air</p>
    </div>
    <div class="band">MQ has and continues to develop partnership agreements with proven and high potential players in c02 reduction space</div>
  </div>
  <footer class="footer"><div class="tab" style="left:0;top:14px;width:8px;height:22px"></div><span class="url">www.marblequill.com</span><span class="name">MarbleQuill</span></footer>
</section>

</body>
</html>
```